Startseite gestalten!
Zielgruppe
20 - 45 Jahre alt, legt Wert auf Mode usw.
Hallo,
ich suche jemanden, der mir die Startseite von K&W stoffwerk (www.kw-stoffwerk.com) chic gestalten kann.
Die Elemente, die jetzt drauf sind sollen bleiben... es geht nur noch um die Gestaltung.
Also Video, Blog und 2 "Werbeflächen" sollen bleiben....
Ebenso die Grundfarbgestaltung usw.
Soll halt schön in die restl. Seite passen.
Freue mich auf die Entwürfe!

```html
<!DOCTYPE html>
<html lang="de">
<head>
<meta charset="utf-8">
<title>K&amp;W stoffwerk – Startseite</title>
<link href="https://fonts.googleapis.com/css2?family=Oswald:wght@300;400;600&display=swap" rel="stylesheet">
<style>
  :root {
    --stage: #3b3b3b;
    --paper: #ffffff;
    --ink: #111111;
    --bar-bottom: #050505;
    --accent-blue: #1a8fd0;
    --sale: #c8104f;
    --photo-grey: #8d949c;
  }
  * { box-sizing: border-box; margin: 0; padding: 0; }
  html, body { width: 1200px; height: 914px; overflow: hidden; }
  body {
    background: var(--stage);
    font-family: "Oswald", "Arial Narrow", sans-serif;
    position: relative;
  }
  .page {
    position: absolute; left: 126px; top: 69px;
    width: 957px; height: 776px;
    background: var(--paper);
    border-radius: 12px;
    overflow: hidden;
  }
  .masthead {
    position: absolute; left: 0; top: 0; width: 957px; height: 156px;
    background: linear-gradient(180deg, #a7adb3 0%, var(--photo-grey) 45%, #6f757d 100%);
  }
  .masthead__players {
    position: absolute; inset: 0;
    background:
      radial-gradient(ellipse 90px 70px at 10% 60%, rgba(20,20,25,.55), transparent 70%),
      radial-gradient(ellipse 110px 80px at 30% 55%, rgba(40,60,100,.45), transparent 70%),
      radial-gradient(ellipse 110px 80px at 72% 55%, rgba(40,60,100,.45), transparent 70%),
      radial-gradient(ellipse 100px 80px at 90% 60%, rgba(20,20,25,.55), transparent 70%);
  }
  .brand {
    position: absolute; left: 0; width: 100%; top: 38px;
    text-align: center; color: #fff;
    font-weight: 400; font-size: 52px; letter-spacing: 1px;
  }
  .lang {
    position: absolute; right: 38px; top: 136px;
    font-size: 12px; font-weight: 300; color: #fff;
  }
  .lang span + span { border-left: 1px solid #fff; margin-left: 6px; padding-left: 6px; }

  .mainnav {
    position: absolute; left: 0; top: 156px; width: 957px; height: 50px;
    display: flex;
    background: linear-gradient(180deg, #f2f2f2 0%, #9a9a9a 30%, #1a1a1a 60%, var(--bar-bottom) 100%);
  }
  .mainnav__item {
    flex: 1; display: flex; align-items: center; justify-content: center;
    color: #fff; font-weight: 300; font-size: 21px;
    border-left: 1px solid #fff;
  }
  .mainnav__item--active {
    flex: 0 0 158px; border-left: none;
    background: linear-gradient(180deg, #777 0%, #222 40%, #000 100%);
    font-weight: 600; height: 56px; border-radius: 0 0 6px 6px;
  }

  .showcase {
    position: absolute; left: 4px; top: 211px; width: 949px; height: 295px;
    border: 2px solid var(--ink); border-radius: 10px;
  }
  .showcase__title {
    position: absolute; top: 0; width: 100%; text-align: center;
    color: var(--accent-blue); font-size: 23px; line-height: 30px;
    font-weight: 300; letter-spacing: .5px;
  }
  .carousel { position: absolute; left: 0; top: 0; }

  .tiles {
    position: absolute; left: 2px; top: 523px;
    display: flex; gap: 6px;
  }
  .tile {
    width: 186px; height: 191px; border-radius: 10px; overflow: hidden;
    background: #000; box-shadow: 0 3px 5px rgba(0,0,0,.35);
    display: flex; flex-direction: column;
  }
  .tile__head {
    height: 30px; flex: none; text-align: center; color: #fff;
    font-weight: 300; font-size: 19px; line-height: 30px;
    background: linear-gradient(180deg, #f0f0f0 0%, #9b9b9b 35%, #222 70%, #000 100%);
  }
  .tile__body { flex: 1; margin: 0 6px 8px; border-radius: 6px; position: relative; overflow: hidden; }
  .tile__media--video { background: linear-gradient(180deg, #b9d1a6 0%, #6f8f5a 55%, #2d3d56 100%); }
  .tile__media--news { background: linear-gradient(160deg, #d9d9d9 0%, #9a9a9a 50%, #3a4a80 100%); }
  .tile__controls {
    position: absolute; left: 0; bottom: 0; width: 100%; height: 16px; background: #e8e8e8;
  }
  .tile__controls::before {
    content: ""; position: absolute; left: 22px; right: 40px; top: 7px; height: 2px; background: #888;
  }
  .tile__play {
    position: absolute; left: 50%; top: 45%; width: 40px; height: 28px; margin: -14px 0 0 -20px;
    background: rgba(255,255,255,.75); border-radius: 5px;
  }
  .tile__play::after {
    content: ""; position: absolute; left: 15px; top: 7px;
    border-left: 13px solid #555; border-top: 7px solid transparent; border-bottom: 7px solid transparent;
  }
  .tile__body--sale {
    background: var(--sale); color: #fff; text-align: center; margin-bottom: 6px;
  }
  .sale__title { font-weight: 600; font-size: 31px; line-height: 38px; margin-top: 4px; white-space: nowrap; }
  .sale__sub { font-weight: 300; font-size: 17px; line-height: 20px; white-space: nowrap; }
  .sale__rates { position: relative; height: 58px; }
  .sale__rates span { position: absolute; font-weight: 300; white-space: nowrap; }
  .sale__small { left: 8px; top: 6px; font-size: 14px; line-height: 18px; }
  .sale__big { left: 32px; top: 12px; font-size: 34px; line-height: 42px; }
  .sale__mid { right: 6px; top: 0; font-size: 26px; line-height: 32px; }
  .sale__groups { font-weight: 300; font-size: 17px; word-spacing: 6px; white-space: nowrap; }

  .footer-rule {
    position: absolute; left: 0; top: 731px; width: 957px; height: 7px; background: var(--ink);
  }
  .footer-links {
    position: absolute; left: 50px; top: 749px; width: 890px;
    display: flex; justify-content: space-between; list-style: none;
    font-size: 15px; font-weight: 300; color: var(--ink);
  }
  .footer-links li::before { content: "• "; }
</style>
</head>
<body>
  <main class="page">
    <header class="masthead">
      <div class="masthead__players" role="img" aria-label="Foto: Polospieler auf Pferden im Spiel"></div>
      <div class="brand">K&amp;W stoffwerk</div>
      <div class="lang"><span>Deutsch</span><span>Englisch</span></div>
    </header>

    <nav class="mainnav">
      <a class="mainnav__item mainnav__item--active">Home</a>
      <a class="mainnav__item">Shop</a>
      <a class="mainnav__item">Charity</a>
      <a class="mainnav__item">About us</a>
      <a class="mainnav__item">Impressionen</a>
      <a class="mainnav__item">Services</a>
    </nav>

    <section class="showcase">
      <h2 class="showcase__title">JETZT NEU IM&nbsp; ONLINE SHOP</h2>
      <svg class="carousel" width="949" height="295" viewBox="130 280 949 295">
        <defs>
          <linearGradient id="cardShade" x1="0" y1="0" x2="0" y2="1">
            <stop offset="0" stop-color="#ffffff"/><stop offset="1" stop-color="#e6e6e6"/>
          </linearGradient>
          <linearGradient id="photoTone" x1="0" y1="0" x2="0" y2="1">
            <stop offset="0" stop-color="#8fc0e8"/><stop offset=".5" stop-color="#5a7aa0"/><stop offset="1" stop-color="#1d2230"/>
          </linearGradient>
          <linearGradient id="track" x1="0" y1="0" x2="0" y2="1">
            <stop offset="0" stop-color="#eeeeee"/><stop offset="1" stop-color="#8a8a8a"/>
          </linearGradient>
        </defs>
        <g stroke="#555" stroke-width="1.2" font-family="Oswald, sans-serif" font-size="15" font-weight="600">
          <g>
            <polygon points="170,326 245,338 245,514 170,520" fill="url(#cardShade)"/>
            <rect x="180" y="357" width="58" height="100" fill="#2e2e2e" stroke="none" role="img" aria-label="Produktbild: schwarzes Poloshirt"/>
            <text x="213" y="502" fill="#111" stroke="none" transform="rotate(6 213 502)">Blindtext</text>
          </g>
          <g>
            <polygon points="243,326 318,338 318,514 243,520" fill="url(#cardShade)"/>
            <rect x="253" y="357" width="58" height="100" fill="#2e2e2e" stroke="none" role="img" aria-label="Produktbild: schwarzes Poloshirt"/>
            <text x="286" y="502" fill="#111" stroke="none" transform="rotate(6 286 502)">Blindtext</text>
          </g>
          <g>
            <polygon points="315,326 443,340 443,510 315,520" fill="url(#cardShade)"/>
            <rect x="328" y="352" width="104" height="110" rx="6" fill="#2e2e2e" stroke="none" role="img" aria-label="Produktbild: schwarzes Poloshirt"/>
            <text x="375" y="496" fill="#111" stroke="none" transform="rotate(-4 375 496)">Blindtext</text>
          </g>
          <g>
            <polygon points="960,340 1035,326 1035,520 960,514" fill="url(#cardShade)"/>
            <rect x="967" y="357" width="58" height="100" fill="#2e2e2e" stroke="none" role="img" aria-label="Produktbild: schwarzes Poloshirt"/>
            <text x="970" y="502" fill="#111" stroke="none">Blindtext</text>
          </g>
          <g>
            <polygon points="893,340 960,326 960,520 893,514" fill="url(#cardShade)"/>
            <rect x="900" y="357" width="54" height="100" fill="#2e2e2e" stroke="none" role="img" aria-label="Produktbild: schwarzes Poloshirt"/>
            <text x="903" y="502" fill="#111" stroke="none">Blindtext</text>
          </g>
          <g>
            <polygon points="768,340 896,326 896,520 768,510" fill="url(#cardShade)"/>
            <rect x="778" y="352" width="104" height="110" rx="6" fill="#2e2e2e" stroke="none" role="img" aria-label="Produktbild: schwarzes Poloshirt"/>
            <text x="780" y="494" fill="#111" stroke="none" transform="rotate(4 780 494)">Blindtext</text>
          </g>
          <rect x="440" y="318" width="330" height="208" rx="10" fill="url(#photoTone)" stroke="#444" role="img" aria-label="Foto: drei Personen in der neuen Polokollektion"/>
        </g>
        <rect x="320" y="549" width="565" height="15" rx="7" fill="url(#track)" stroke="#555"/>
        <rect x="440" y="550" width="142" height="13" rx="6" fill="#3a3a3a"/>
        <rect x="320" y="549" width="24" height="15" rx="4" fill="#ddd" stroke="#555"/>
        <polygon points="337,551 327,556.5 337,562" fill="#111"/>
        <rect x="861" y="549" width="24" height="15" rx="4" fill="#ddd" stroke="#555"/>
        <polygon points="868,551 878,556.5 868,562" fill="#111"/>
        <rect x="1005" y="549" width="30" height="16" rx="3" fill="#111"/>
        <polygon points="1016,552 1009,557 1016,562" fill="#fff"/>
        <polygon points="1024,552 1031,557 1024,562" fill="#fff"/>
      </svg>
    </section>

    <section class="tiles">
      <article class="tile">
        <div class="tile__head">Making of</div>
        <div class="tile__body tile__media--video" role="img" aria-label="Video: Making-of mit Pferd und Spielern">
          <div class="tile__play"></div>
          <div class="tile__controls"></div>
        </div>
      </article>
      <article class="tile">
        <div class="tile__head">News</div>
        <div class="tile__body tile__media--news" role="img" aria-label="Bild: Teamshirt-Kollektion mit Spieler in Poloausrüstung"></div>
      </article>
      <article class="tile">
        <div class="tile__head">Sale</div>
        <div class="tile__body tile__body--sale">
          <div class="sale__title">Herbst Sale</div>
          <div class="sale__sub">Attraktive Vorteilspreise</div>
          <div class="sale__rates">
            <span class="sale__small">-15%</span>
            <span class="sale__big">-30%</span>
            <span class="sale__mid">-40%</span>
          </div>
          <div class="sale__groups">Damen Herren Kinder</div>
        </div>
      </article>
      <article class="tile">
        <div class="tile__head">Presse</div>
        <div class="tile__body"></div>
      </article>
      <article class="tile">
        <div class="tile__head">Kariere</div>
        <div class="tile__body"></div>
      </article>
    </section>

    <div class="footer-rule"></div>
    <ul class="footer-links">
      <li>Link</li>
      <li>Kontakt</li>
      <li>Newsletter</li>
      <li>Impressum</li>
      <li>AGB</li>
      <li>Datenschutzerklärung</li>
    </ul>
  </main>
</body>
</html>
```